Chocolate Bar Design

I need packaging design for a new line of chocolate bars.

The new design must fit in with the packaging design for our line of solid chocolate bars. The previous bars are packaged in clear boxes, the new line is in 3x3 kraft boxes so the new design must be visusally appealing, and portray what lies inside as they are not able to view the bar itself.

The new product line is for "Truffle Bars", basically a chocolate bar with a truffle filling. The first three flavors are Orchid Ember (Cinnamon and Cayenne, Sea Salt), Cafe Mocha, and Pumpkin Pie.

These are artisan bars, and should reflect in the packaging.

If you view our previous packaging, they are the same design but with a different color for each flavor, which would be ideal.

Industry/Entity Type

Cafe

Requirements
Must have
• Each design should include the front label that has the company name, size of the bar, and name of the bar at minimum. The reverse label must have company name, address, website, and ingredients, at minimum.

Nice to have
• Ideally, I would be able to edit ingredients, and bar names easily.

```html
<!DOCTYPE html>
<html lang="en">
<head>
<meta charset="utf-8">
<title>Harlan Vale Chocolates – Truffle Bar Labels</title>
<link rel="stylesheet" href="https://fonts.googleapis.com/css2?family=Tinos:wght@400;700&family=Arimo:wght@700&display=swap">
<style>
  :root {
    --kraft-gold: #c4a05f;
    --label-white: #ffffff;
    --ink: #1a1a1a;
    --title-band: #151515;
    --title-text: #ffffff;
    --page: #ffffff;
  }
  * { box-sizing: border-box; margin: 0; padding: 0; }
  html, body {
    width: 1200px;
    height: 427px;
    overflow: hidden;
    background: var(--page);
  }
  .label-sheet {
    position: relative;
    width: 1200px;
    height: 427px;
  }
  .bar-label {
    position: absolute;
    top: 27px;
    width: 370px;
    height: 370px;
    background: var(--kraft-gold);
  }
  .bar-label--mocha { left: 27px; }
  .bar-label--ember { left: 415px; }
  .bar-label--pumpkin { left: 803px; }

  .label-card {
    position: absolute;
    left: 30px;
    top: 30px;
    width: 310px;
    height: 308px;
    background: var(--label-white);
    border-radius: 18px;
    color: var(--ink);
  }
  .brand-name {
    position: absolute;
    top: 24px;
    left: 0;
    width: 100%;
    text-align: center;
    font-family: 'Tinos', 'Times New Roman', serif;
    font-weight: 400;
    font-size: 27px;
    letter-spacing: 0.5px;
    color: var(--ink);
  }
  .flavor-title {
    position: absolute;
    top: 81px;
    left: 32px;
    width: 246px;
    height: 35px;
    background: var(--title-band);
    color: var(--title-text);
    font-family: 'Tinos', 'Times New Roman', serif;
    font-weight: 700;
    font-size: 25px;
    line-height: 35px;
    text-align: center;
  }
  .bar-description {
    position: absolute;
    top: 123px;
    left: 0;
    width: 100%;
    text-align: center;
    font-family: 'Arimo', Arial, sans-serif;
    font-weight: 700;
    font-size: 12.5px;
    line-height: 16px;
  }
  .ingredients {
    position: absolute;
    top: 156px;
    left: 32px;
    width: 248px;
    font-family: 'Tinos', 'Times New Roman', serif;
    font-size: 10.8px;
    letter-spacing: -0.3px;
    line-height: 15.8px;
    text-align: justify;
  }
  .ingredients strong { font-weight: 700; }
  .net-weight {
    position: absolute;
    top: 244px;
    left: 30px;
    width: 64px;
    text-align: center;
    font-family: 'Tinos', 'Times New Roman', serif;
    font-size: 12.5px;
    line-height: 14.5px;
  }
  .maker-contact {
    position: absolute;
    top: 239px;
    left: 131px;
    font-family: 'Tinos', 'Times New Roman', serif;
    font-size: 11.5px;
    line-height: 15px;
    font-style: normal;
    white-space: nowrap;
  }
  .maker-contact .web { font-weight: 700; }
</style>
</head>
<body>
<main class="label-sheet">

  <section class="bar-label bar-label--mocha">
    <div class="label-card">
      <p class="brand-name">Harlan Vale Chocolates</p>
      <h2 class="flavor-title">Cafe Mocha</h2>
      <p class="bar-description">Exclusively Hand-Crafted<br>Chocolate Bar with Truffle filling</p>
      <p class="ingredients"><strong>INGREDIENTS:</strong> Lum excerum, ullabor epeditat harupti rem aliquia eptatem voluptat rem ant est as et vent ut a quisita esequis dolupta nis que num as esciend uscilis es duntio oditemp oresent ullestium et excest, con pero de molo ium fugiaspis nobisi diti volut perum, quidusdant.</p>
      <p class="net-weight">NET WT.<br>2,5 OZ<br>70 G</p>
      <address class="maker-contact">Harlan Vale Chocolates<br>&lt;&lt;Address_1&gt;&gt;, Fernwick, OR<br>info@harlanvalechocolates.com<br><span class="web">harlanvalechocolates.com</span></address>
    </div>
  </section>

  <section class="bar-label bar-label--ember">
    <div class="label-card">
      <p class="brand-name">Harlan Vale Chocolates</p>
      <h2 class="flavor-title">Orchid Ember</h2>
      <p class="bar-description">Exclusively Hand-Crafted<br>Chocolate Bar with Truffle filling</p>
      <p class="ingredients"><strong>INGREDIENTS:</strong> Lum excerum, ullabor epeditat harupti rem aliquia eptatem voluptat rem ant est as et vent ut a quisita esequis dolupta nis que num as esciend uscilis es duntio oditemp oresent ullestium et excest, con pero de molo ium fugiaspis nobisi diti volut perum, quidusdant.</p>
      <p class="net-weight">NET WT.<br>2,5 OZ<br>70 G</p>
      <address class="maker-contact">Harlan Vale Chocolates<br>&lt;&lt;Address_1&gt;&gt;, Fernwick, OR<br>info@harlanvalechocolates.com<br><span class="web">harlanvalechocolates.com</span></address>
    </div>
  </section>

  <section class="bar-label bar-label--pumpkin">
    <div class="label-card">
      <p class="brand-name">Harlan Vale Chocolates</p>
      <h2 class="flavor-title">Pumpkin Pie</h2>
      <p class="bar-description">Exclusively Hand-Crafted<br>Chocolate Bar with Truffle filling</p>
      <p class="ingredients"><strong>INGREDIENTS:</strong> Lum excerum, ullabor epeditat harupti rem aliquia eptatem voluptat rem ant est as et vent ut a quisita esequis dolupta nis que num as esciend uscilis es duntio oditemp oresent ullestium et excest, con pero de molo ium fugiaspis nobisi diti volut perum, quidusdant.</p>
      <p class="net-weight">NET WT.<br>2,5 OZ<br>70 G</p>
      <address class="maker-contact">Harlan Vale Chocolates<br>&lt;&lt;Address_1&gt;&gt;, Fernwick, OR<br>info@harlanvalechocolates.com<br><span class="web">harlanvalechocolates.com</span></address>
    </div>
  </section>

</main>
</body>
</html>
```